Meadow Lantern Veterinary Practice including Nest2Grow

We require a double-sided full colour tri-fold Brochure for Print.
Colour theme to in line with logo below

Written CONTENT below
Orphans
We can provide care and a new mother for orphan foals of any age, breed or size, from thoroughbreds and draft breeds to tiny ponies and even donkeys.
We have successfully fostered orphans from a few hours of age through to eight weeks, regardless of how long or if at all they were with their birth mother, and of previous fostering attempts.
We have the knowledge and experience to provide optimum nutrition and care to orphans during the brief period that they don’t have a mum, until their new foster mother is ready to take them.
Additionally we are a veterinary practice, and can provide diagnostics and therapeutics for compromised orphan foals such as plasma administration and health checks.

Mares
Nest2Grow mares have been selected for mothering ability and temperament, and have all carried and raised at least one foal of their own. Many have already been successful foster mothers in one or more of the last five breeding seasons.
The mares are not currently pregnant and are given a carefully designed course of hormones to induce lactation when required. The milk produced is not colostrum, but is completely normal and equivalent to that which they would have had if the foal was theirs by birth.
There is published scientific information (in addition to our own experience and that of the owners of previous graduates of our programme) that growth and development of foals raised by induced lactation is identical to that of foals raised by their birth mothers.

Fostering
During the few days when the mare’s udder is developing, mare and foal are kept next separately but in close proximity, allowing bonding to begin and reducing stress on the orphan.
The fostering is completed once the mare has enough milk to feed the foal, and our experienced handlers ensure that joining the two goes smoothly.
Once they are together the mare completely accepts the foal as her own, and the foal can suckle freely – at this stage we continue to offer supplementary feeds until they are not needed.
The mare and foal are then a normal unit and can return to the foal owner’s care until weaning – ensuring optimum nutrition and behaviour for the foal and excellent outcomes in performance, relationships with other horses, and interaction with humans.

Complete Safety
Mares recognise their birth foal by scent - a unique bond established during the first few minutes of the foal’s life - and only a small percentage of mares who have lost their own foal will readily accept a substitute.
When a mare who has lost her birth foal is offered an orphan, it is very normal and common for her to respond with aggression - to the danger of the foal and the human handler.
Nest2Grow mares have no birth foal in the current season, and are happy to adopt any foal who is placed close to them during the hormone treatment period.
This makes for total foal and handler safety.

Excellent Success Rate
After seven years of perfecting the fostering method, Nest2Grow can claim total success: we have now documented almost 50 fosterings over the last five breeding seasons. We have never been entrusted with an orphan foal that we have not been able to provide with a beautiful foster mum.

Career Mothers
Being dedicated career mothers with no other job in life, our mares are free to accompany their new foals home and stay with them as long as required. No foals are weaned and left without a mother in our programme, and our beautiful mares who would otherwise not be bred, are given a foal every year and a wonderful lifelong purpose.

Every single orphan’s human family has admired and appreciated our beautiful mares, with many offering to give them a home for life. Each season as the orphans are weaned, we welcome our mares home to Meadow Lantern to prepare for the next foal in need – a job they totally love! – just as if they were in a natural breeding situation.

Meadow Lantern Vet Practice including Nest2Grow
214 Pellerby Lane
Thornvale. Vic. 3812

Phone 0431958617 or 0419284056

```html
<!DOCTYPE html>
<html lang="en">
<head>
<meta charset="utf-8">
<title>Meadow Lantern Veterinary Practice – Tri-fold Brochure</title>
<link href="https://fonts.googleapis.com/css2?family=Lato:wght@400;700;900&display=swap" rel="stylesheet">
<style>
  :root{
    --orange:#f39220;
    --orange-deep:#ef6f1a;
    --orange-light:#f7b24a;
    --ink:#333333;
    --charcoal:#4a4a4f;
    --paper:#ffffff;
    --paper-grey:#ececec;
    --backdrop:#3b3b3b;
  }
  *{box-sizing:border-box;margin:0;padding:0}
  html,body{width:1200px;height:2525px;overflow:hidden}
  body{background:var(--backdrop);font-family:'Lato',sans-serif;color:var(--ink);position:relative}
  .spread{position:absolute;left:50px;width:1100px;height:856px;background:var(--paper);overflow:hidden;box-shadow:0 6px 18px rgba(0,0,0,.45)}
  .spread--outside{top:380px}
  .spread--inside{top:1300px}
  .spread__shapes{position:absolute;left:0;top:0;width:1100px;height:856px}
  .column{position:absolute;top:0;height:856px;padding:38px 28px 0}
  .col-1{left:0;width:367px}
  .col-2{left:367px;width:366px}
  .col-3{left:733px;width:367px}
  .heading{display:flex;align-items:center;gap:12px;margin-bottom:10px}
  .heading svg{width:34px;height:20px;flex:none}
  .heading__title{font-weight:900;font-size:27px;letter-spacing:.5px;text-transform:uppercase;color:var(--ink);line-height:1}
  .heading__sub{display:block;font-weight:400;font-size:25px;margin-top:3px}
  .heading--stack{align-items:flex-start}
  .heading--stack svg{margin-top:4px}
  .body-text p{font-size:12.4px;line-height:1.38;text-align:justify;margin-bottom:12px}
  .body-text--tight p{font-size:11.8px;line-height:1.36;margin-bottom:10px}
  .address{position:absolute;left:0;width:366px;top:745px;text-align:center;font-size:19px;line-height:1.3;color:var(--ink)}
  .address__phone{font-weight:700;font-size:25px;margin-top:4px}
  .brand{position:absolute;left:775px;top:78px;width:310px}
  .brand__name{font-weight:400;font-size:35px;color:var(--orange-deep);line-height:1}
  .brand__tag{font-size:10px;letter-spacing:4px;color:var(--orange);margin-top:4px;padding-left:60px;text-transform:uppercase}
  .cover-title{position:absolute;left:733px;top:722px;width:367px;text-align:center}
  .cover-title__name{font-weight:900;font-size:34px;color:#fff}
  .cover-title__tag{font-size:19px;color:var(--orange);margin-top:6px}
  .call{position:absolute;left:770px;top:798px;width:310px;text-align:right;font-weight:900;font-size:27px;color:#fff}
</style>
</head>
<body>

<!-- Outside spread -->
<section class="spread spread--outside">
  <svg class="spread__shapes" viewBox="0 0 1100 856" aria-hidden="false">
    <defs>
      <linearGradient id="greyPanel" x1="0" y1="0" x2="1" y2="0">
        <stop offset="0" stop-color="#dcdcdc"/><stop offset=".5" stop-color="#f7f7f7"/><stop offset="1" stop-color="#e2e2e2"/>
      </linearGradient>
      <linearGradient id="orangeGrad" x1="0" y1="0" x2="1" y2="1">
        <stop offset="0" stop-color="#f7a531"/><stop offset="1" stop-color="#ef6f1a"/>
      </linearGradient>
    </defs>
    <rect x="367" y="0" width="366" height="856" fill="var(--paper-grey)"/>
    <rect x="733" y="0" width="367" height="856" fill="url(#greyPanel)"/>
    <rect x="0" y="0" width="1100" height="16" fill="url(#orangeGrad)"/>
    <!-- bottom-left orange disc -->
    <circle cx="185" cy="720" r="200" fill="url(#orangeGrad)"/>
    <circle cx="211" cy="690" r="146" fill="#fff"/>
    <circle cx="211" cy="690" r="136" fill="#8a8f5a" role="img" aria-label="Photo: a girl leading a chestnut horse on grass"/>
    <!-- career mothers photo -->
    <circle cx="495" cy="567" r="100" fill="none" stroke="var(--orange)" stroke-width="3"/>
    <circle cx="495" cy="567" r="92" fill="#7d7a58" role="img" aria-label="Photo: a mare and her foal standing in a paddock"/>
    <!-- cover photo -->
    <path d="M640 453 A227 227 0 0 1 1094 453" fill="none" stroke="var(--orange)" stroke-width="16"/>
    <circle cx="867" cy="453" r="232" fill="#fff"/>
    <circle cx="867" cy="453" r="222" fill="#6f6a5c" role="img" aria-label="Photo: a vet bottle-feeding an orphan foal in a stable"/>
    <rect x="733" y="690" width="367" height="166" fill="var(--charcoal)"/>
  </svg>

  <div class="column col-1 body-text">
    <div class="heading">
      <svg viewBox="0 0 34 20"><path d="M0 0h10l8 10-8 10H0l8-10z M14 0h10l8 10-8 10H14l8-10z" fill="var(--orange)"/></svg>
      <span class="heading__title">Fostering</span>
    </div>
    <p>Mares recognise their birth foal by scent - a unique bond established during the first few minutes of the foal's life - and only a small percentage of mares who have lost their own foal will readily accept a substitute.</p>
    <p>When a mare who has lost her birth foal is offered an orphan, it is very normal and common for her to respond with aggression - to the danger of the foal and the human handler.</p>
    <p>Nest2Grow mares have no birth foal in the current season, and are happy to adopt any foal who is placed close to them during the hormone treatment period. This makes for total foal and handler safety.</p>
    <div class="heading heading--stack" style="margin-top:20px">
      <svg viewBox="0 0 34 20"><path d="M0 0h10l8 10-8 10H0l8-10z M14 0h10l8 10-8 10H14l8-10z" fill="var(--orange)"/></svg>
      <span class="heading__title">Excellent<span class="heading__sub">SUCCESS RATE</span></span>
    </div>
    <p>After seven years of perfecting the fostering method, Nest2Grow can claim total success: we have now documented almost 50 fosterings over the last five breeding seasons. We have never been entrusted with an orphan foal that we have not been able to provide with a beautiful foster mum.</p>
  </div>

  <div class="column col-2 body-text">
    <div class="heading heading--stack">
      <svg viewBox="0 0 34 20"><path d="M0 0h10l8 10-8 10H0l8-10z M14 0h10l8 10-8 10H14l8-10z" fill="var(--orange)"/></svg>
      <span class="heading__title">Career<span class="heading__sub">MOTHERS</span></span>
    </div>
    <p>Being dedicated career mothers with no other job in life, our mares are free to accompany their new foals home and stay with them as long as required. No foals are weaned and left without a mother in our programme, and our beautiful mares who would otherwise not be bred, are given a foal every year and a wonderful lifelong purpose.</p>
    <p>Every single orphan's human family has admired and appreciated our beautiful mares, with many offering to give them a home for life. Each season as the orphans are weaned, we welcome our mares home to Meadow Lantern to prepare for the next foal in need – a job they totally love! – just as if they were in a natural breeding situation.</p>
  </div>
  <div class="address" style="left:367px">
    214 Pellerby Lane<br>Thornvale, Victoria, Australia
    <div class="address__phone">Call +61 431 958 617</div>
  </div>

  <div class="brand">
    <div class="brand__name">Meadow Lantern</div>
    <div class="brand__tag">Veterinary Practice</div>
  </div>
  <div class="cover-title">
    <div class="cover-title__name">Meadow Lantern</div>
    <div class="cover-title__tag">Veterinary Practice</div>
  </div>
</section>

<!-- Inside spread -->
<section class="spread spread--inside">
  <svg class="spread__shapes" viewBox="0 0 1100 856">
    <defs>
      <linearGradient id="orangeGrad2" x1="0" y1="0" x2="1" y2="1">
        <stop offset="0" stop-color="#f7a531"/><stop offset="1" stop-color="#ef6f1a"/>
      </linearGradient>
    </defs>
    <rect x="0" y="0" width="367" height="16" fill="url(#orangeGrad2)"/>
    <rect x="733" y="0" width="367" height="16" fill="url(#orangeGrad2)"/>
    <!-- left orange backing -->
    <path d="M0 470 Q140 430 250 520 Q370 640 340 856 L0 856 Z" fill="url(#orangeGrad2)"/>
    <circle cx="252" cy="475" r="73" fill="#fff"/>
    <circle cx="252" cy="475" r="66" fill="#9a6a3e" role="img" aria-label="Photo: head of a chestnut foal"/>
    <circle cx="190" cy="670" r="168" fill="#fff"/>
    <circle cx="190" cy="670" r="158" fill="#7f8560" role="img" aria-label="Photo: a mare with a small foal in a fenced paddock"/>
    <!-- centre top orange half disc -->
    <circle cx="556" cy="120" r="215" fill="url(#orangeGrad2)"/>
    <circle cx="556" cy="186" r="156" fill="#fff"/>
    <circle cx="556" cy="186" r="148" fill="#6d6e58" role="img" aria-label="Photo: a handler standing with a dark mare and foal"/>
    <circle cx="461" cy="350" r="58" fill="#fff"/>
    <circle cx="461" cy="350" r="52" fill="#6b5d4a" role="img" aria-label="Photo: a foal resting in straw"/>
    <circle cx="535" cy="385" r="56" fill="#fff"/>
    <circle cx="535" cy="385" r="50" fill="#7a6a52" role="img" aria-label="Photo: mare and foal grazing"/>
    <circle cx="668" cy="328" r="56" fill="#fff"/>
    <circle cx="668" cy="328" r="50" fill="#8a6446" role="img" aria-label="Photo: a foal lying beside its foster mare"/>
    <!-- phone band -->
    <path d="M733 856 L733 800 Q733 765 775 765 L1100 765 L1100 856 Z" fill="url(#orangeGrad2)"/>
  </svg>

  <div class="column col-1 body-text">
    <div class="heading">
      <svg viewBox="0 0 34 20"><path d="M0 0h10l8 10-8 10H0l8-10z M14 0h10l8 10-8 10H14l8-10z" fill="var(--orange)"/></svg>
      <span class="heading__title">Orphans</span>
    </div>
    <p>We can provide care and a new mother for orphan foals of any age, breed or size, from thoroughbreds and draft breeds to tiny ponies and even donkeys.</p>
    <p>We have successfully fostered orphans from a few hours of age through to eight weeks, regardless of how long or if at all they were with their birth mother, and of previous fostering attempts.</p>
    <p>We have the knowledge and experience to provide optimum nutrition and care to orphans during the brief period that they don't have a mum, until their new foster mother is ready to take them.</p>
    <p>Additionally we are a veterinary practice, and can provide diagnostics and therapeutics for compromised orphan foals such as plasma administration and health checks.</p>
  </div>

  <div class="column col-2 body-text body-text--tight" style="padding-top:455px">
    <div class="heading">
      <svg viewBox="0 0 34 20"><path d="M0 0h10l8 10-8 10H0l8-10z M14 0h10l8 10-8 10H14l8-10z" fill="var(--orange)"/></svg>
      <span class="heading__title">Mares</span>
    </div>
    <p>Nest2Grow mares have been selected for mothering ability and temperament, and have all carried and raised at least one foal of their own. Many have already been successful foster mothers in one or more of the last five breeding seasons.</p>
    <p>The mares are not currently pregnant, and are given a carefully designed course of hormones to induce lactation when required. The milk produced is not colostrum, but is completely normal and equivalent to that which they would have had if the foal was theirs by birth.</p>
    <p>There is published scientific information (in addition to our own experience and that of the owners of previous graduates of our programme) that growth and development of foals raised by induced lactation is identical to that of foals raised by their birth mothers.</p>
  </div>

  <div class="column col-3 body-text body-text--tight">
    <div class="heading">
      <svg viewBox="0 0 34 20"><path d="M0 0h10l8 10-8 10H0l8-10z M14 0h10l8 10-8 10H14l8-10z" fill="var(--orange)"/></svg>
      <span class="heading__title">Fostering</span>
    </div>
    <p>We can provide care and a new mother for orphan foals of any age, breed or size, from thoroughbreds and During the few days when the mare's udder is developing, mare and foal are kept next separately but in close proximity, allowing bonding to begin and reducing stress on the orphan.</p>
    <p>The fostering is completed once the mare has enough milk to feed the foal, and our experienced handlers ensure that joining the two goes smoothly.</p>
    <p>Once they are together the mare completely accepts the foal as her own, and the foal can suckle freely – at this stage we continue to offer supplementary feeds until they are not needed.</p>
    <p>The mare and foal are then a normal unit and can return to the foal owner's care until weaning – ensuring optimum nutrition and behaviour for the foal and excellent outcomes in performance, relationships with other horses, and interaction with humans.<br>draft breeds to tiny ponies and even donkeys.</p>
    <p>We have successfully fostered orphans from a few hours of age through to eight weeks, regardless of how long or if at all they were with their birth mother, and of previous fostering attempts.</p>
    <p>We have the knowledge and experience to provide optimum nutrition and care to orphans during the brief period that they don't have a mum, until their new foster mother is ready to take them.</p>
    <p>Additionally we are a veterinary practice, and can provide diagnostics and therapeutics for compromised orphan foals such as plasma administration and health checks.</p>
  </div>
  <div class="call">Call +61 431 958 617</div>
</section>

</body>
</html>
```